Brisa Pastry Mill Business card

We are empanada whole-sellers and I want a business card design with a picture of an empanada on it that also mentions first trial order FREE. our contact number 555-214-7093 our website www.brisapastry.example and business email Tobin@brisapastry.example

If you want any of our artwork please feel free to email me at the address above.

```html
<!DOCTYPE html>
<html lang="en">
<head>
<meta charset="utf-8">
<title>Brisa Pastry Mill — Business Card</title>
<link rel="stylesheet" href="https://fonts.googleapis.com/css2?family=Arvo:wght@400;700&family=Archivo+Black&family=Archivo:wght@700;800&display=swap">
<style>
  :root {
    --bg: #1e1e1f;
    --card-tint: #f1f2f4;
    --yellow: #e8b92a;
    --yellow-deep: #c99a17;
    --ink: #141414;
    --white: #ffffff;
    --pastry-light: #e6c795;
    --pastry-mid: #d4b07a;
    --pastry-dark: #9c8a8a;
  }
  * { box-sizing: border-box; margin: 0; padding: 0; }
  html, body { width: 1200px; height: 800px; overflow: hidden; }
  body {
    background: var(--bg);
    position: relative;
    font-family: "Archivo", sans-serif;
  }
  .card {
    position: absolute;
    top: 257px;
    width: 500px;
    height: 286px;
    background: var(--card-tint);
    border-radius: 3px;
    overflow: hidden;
  }
  .card--back { left: 80px; }
  .card--front { left: 620px; }

  /* Back */
  .offer {
    position: absolute;
    top: 28px; left: 0; right: 0;
    text-align: center;
    color: var(--ink);
    font-family: "Arvo", serif;
    white-space: nowrap;
  }
  .offer__lead { font-size: 20px; font-weight: 700; vertical-align: 3px; }
  .offer__free { font-size: 38px; font-weight: 700; letter-spacing: 1px; margin-left: 6px; }
  .trim {
    position: absolute;
    left: 70px; right: 70px;
    display: flex; flex-direction: column;
  }
  .trim__bar { height: 5px; background: var(--yellow); }
  .trim__band { height: 7px; background: var(--ink); }
  .trim--top { top: 80px; }
  .trim--bottom { bottom: 34px; }
  .trim--bottom .trim__band { order: -1; }
  .product-photo {
    position: absolute;
    top: 92px; left: 120px;
    width: 260px; height: 152px;
    border-radius: 50%;
    background: radial-gradient(ellipse at 55% 45%, var(--pastry-light) 0%, var(--pastry-mid) 45%, var(--pastry-dark) 100%);
  }

  /* Front */
  .ribbon {
    position: absolute;
    left: 0; top: 0;
    width: 500px; height: 286px;
  }
  .brand {
    position: absolute;
    top: 76px; left: 0; right: 0;
    text-align: center;
    font-family: "Arvo", serif;
    font-weight: 700;
    font-size: 38px;
    color: var(--ink);
    line-height: 1;
    white-space: nowrap;
  }
  .tagline {
    position: absolute;
    top: 124px; left: 0; right: 0;
    text-align: center;
    font-family: "Archivo Black", sans-serif;
    font-size: 11px;
    letter-spacing: 1px;
    color: var(--ink);
  }
  .contact {
    position: absolute;
    top: 145px; left: 0; right: 0;
    text-align: center;
    color: var(--ink);
    font-weight: 800;
    line-height: 1.2;
  }
  .contact__phone { font-size: 22px; letter-spacing: 1px; color: var(--white); line-height: 1.1; }
  .contact__web,
  .contact__email { font-size: 12px; margin-top: 2px; }
  .contact__handle {
    font-size: 10px; margin-top: 3px;
    display: inline-flex; align-items: center; gap: 5px;
  }
  .contact__handle::before {
    content: ""; width: 9px; height: 9px; background: var(--ink);
  }
  .ornament {
    position: absolute;
    top: 134px;
    width: 20px; height: 20px;
    border-radius: 50%;
    background: var(--ink);
  }
  .ornament--left { left: 52px; }
  .ornament--right { right: 52px; }
</style>
</head>
<body>

  <section class="card card--back" aria-label="Business card, back">
    <p class="offer"><span class="offer__lead">First Trial Order</span><span class="offer__free">FREE</span></p>
    <div class="trim trim--top"><div class="trim__bar"></div><div class="trim__band"></div></div>
    <div class="product-photo" role="img" aria-label="Photo of golden baked empanadas on a tray"></div>
    <div class="trim trim--bottom"><div class="trim__bar"></div><div class="trim__band"></div></div>
  </section>

  <section class="card card--front" aria-label="Business card, front">
    <svg class="ribbon" viewBox="0 0 500 286" aria-hidden="true">
      <polygon points="30,30 470,30 456,44 44,44" fill="var(--yellow-deep)"/>
      <polygon points="30,256 470,256 456,242 44,242" fill="var(--yellow-deep)"/>
      <rect x="44" y="30" width="412" height="226" fill="var(--yellow)"/>
      <rect x="44" y="30" width="14" height="226" fill="var(--yellow-deep)"/>
      <rect x="442" y="30" width="14" height="226" fill="var(--yellow-deep)"/>
      <rect x="58" y="44" width="384" height="7" fill="var(--ink)"/>
      <rect x="58" y="235" width="384" height="7" fill="var(--ink)"/>
    </svg>
    <div class="ornament ornament--left" role="img" aria-label="Small flower ornament"></div>
    <div class="ornament ornament--right" role="img" aria-label="Small flower ornament"></div>
    <h1 class="brand">Brisa Pastry Mill</h1>
    <p class="tagline">EMPANADA WHOLESALE &amp; PASTRY</p>
    <div class="contact">
      <p class="contact__phone">555-214-7093</p>
      <p class="contact__web">www.brisapastry.example</p>
      <p class="contact__email">Tobin@brisapastry.example</p>
      <p class="contact__handle">@BRISAPASTRY</p>
    </div>
  </section>

</body>
</html>
```